PACKAGE DESIGN , BOX DESIGN

I've uploaded one of our other boxes so you have a template for this project since the box size is the same. Please use it
Please choose fonts you feel work best.
I think I will like the box light lavender CMYK : C:0.14, M:0.18, Y:0, K:0.
My vision for the design is clean, simple/modern, and professional , upclass.
MAIN DISPLAY/INFO :
LOGO) MORVEN WITH LEAF (file uploaded)
(the logo will be printed in spot foil, im thinking gold with green leaf or lavender with green leaf)
B O T A N I C A L
relieving bath soak
500 MG CBD NET WT. 135 G (4.76 oz)
SIDE PANELS :
MORVEN'S relieving CBD bath bomb is small-batch crafted with intention to thoroughly pamper and replenish your skin and spirit. The intrinsic experience is indulgent with natural butters and beneficial botanical oils to relax the mind and relieve the body. Encompass yourself with these skin-loving ingredients and the enchanting aroma, while making self-care a survival strategy in which you luxuriate yourself with the rejuvenating power of nature.
DIRECTIONS FOR USE : Get Naked.
Fill the tub with exceptionally warm water until it reaches midway. Introduce the bomb to the water and allow it to fully dissolve, before immersing yourself into the luxurious organic bath you've created. Soak up to 20 minutes allowing the bath to transcend the ordinary and transport you to higher, more abundant vibrations.
ICONS :
VEGAN , NATURAL INGREDIENTS, HANDMADE , LAB TESTED
INGREDIENTS: BAKING SODA, CORN STARCH, CITRIC ACID, COCOA BUTTER, MANGO BUTTER, SHEA BUTTER, KAOLIN CLAY, CASTOR OIL, COCONUT OIL, THERAPEUTIC-GRADE ESSENTIAL OILS (LAVANDULA ANGUSTIFOLIA & EUCALYPTUS RADIATA ), PURE CBD CRYSTALLINE, PURPLE SWEET POTATO (NATURAL COLOR), COCO BETAINE, SODIUM LAURYL SULFOACETATE
FOR EXTERNAL USE ONLY.
SAFETY : USE CAUTION WHEN EXITING THE BATH. THESE SKIN LOVING OILS CAN MAKE THE TUB SLIPPERY.
(small print :)
WARNING : THIS PRODUCT IS INTENDED FOR INDIVIDUALS 18 YRS OF AGE OR OLDER. THIS PRODUCT IS NOT INTENDED TO DIAGNOSE, TREAT, OR MITIGATE ANY DISEASE OR CONDITION. CONSULT WITH YOUR PHYSICIAN BEFORE USING THIS PRODUCT ESPECIALLY IF YOU HAVE A MEDICAL CONDITION, IF YOU TAKE PRESCRIPTION MEDICATIONS OR IF YOU ARE PREGNANT OR NURSING.
MORVEN CB DISTRO LLC
LICENSE # QTRW-583094
www.MORVENCBD.example

```html
<!DOCTYPE html>
<html lang="en">
<head>
<meta charset="utf-8">
<title>MORVEN Botanical Relieving Bath Bomb – Box Front</title>
<link rel="stylesheet" href="https://fonts.googleapis.com/css2?family=Archivo+Black&family=Archivo:wght@300;400;700&family=Dancing+Script:wght@500&display=swap">
<style>
  :root {
    --canvas-bg: #ecebef;
    --box-lavender: #c2a4c8;
    --brand-lavender: #b48fc0;
    --frame-lavender: #b899c4;
    --panel-white: #ffffff;
    --botanical-green: #7fb27f;
    --subtitle-grey: #6f6f72;
    --tagline-blue: #6d9bd2;
    --band-text: #ffffff;
  }
  * { margin: 0; padding: 0; box-sizing: border-box; }
  html, body {
    width: 900px; height: 1200px; overflow: hidden;
    background: var(--canvas-bg);
  }
  .box-front {
    position: absolute;
    left: 40px; top: 168px;
    width: 820px; height: 863px;
    background: var(--panel-white);
    overflow: hidden;
  }
  .box-shapes { position: absolute; inset: 0; }
  .brand-name {
    position: absolute; left: 0; right: 0; top: 168px;
    text-align: center;
    font-family: "Archivo Black", "Arial Black", sans-serif;
    font-size: 118px; line-height: 1;
    letter-spacing: -3px;
    color: var(--brand-lavender);
  }
  .product-line {
    position: absolute; left: 0; right: 0; top: 314px;
    text-align: center;
    font-family: "Archivo Black", "Arial Black", sans-serif;
    font-size: 60px; line-height: 1;
    letter-spacing: -1px;
    color: var(--botanical-green);
  }
  .product-type {
    position: absolute; left: 0; right: 0; top: 364px;
    text-align: center;
    font-family: "Archivo", Arial, sans-serif;
    font-weight: 300;
    font-size: 34px; line-height: 1;
    letter-spacing: -0.5px;
    color: var(--subtitle-grey);
  }
  .tagline {
    position: absolute; left: 0; right: 0; top: 420px;
    text-align: center;
    font-family: "Dancing Script", cursive;
    font-size: 17px; line-height: 29px;
    color: var(--tagline-blue);
  }
  .botanical-art {
    position: absolute; left: 298px; top: 485px;
    width: 223px; height: 223px;
    border-radius: 45% 45% 40% 40%;
    background: radial-gradient(ellipse at 50% 45%, #9dbf96 0%, #b9c9b0 35%, #d7cbe3 62%, rgba(230,222,240,0) 78%);
  }
  .benefits {
    position: absolute; left: 0; right: 0; top: 740px;
    text-align: center;
    font-family: "Archivo", Arial, sans-serif;
    font-weight: 300;
    font-size: 24px; line-height: 1;
    letter-spacing: -0.3px;
    color: var(--brand-lavender);
  }
  .info-band {
    position: absolute; left: 0; right: 0; bottom: 0;
    height: 63px;
    background: var(--box-lavender);
    display: flex; align-items: center; justify-content: center;
    font-family: "Archivo", Arial, sans-serif;
    font-weight: 700;
    font-size: 23px;
    letter-spacing: -0.3px;
    color: var(--band-text);
  }
</style>
</head>
<body>
  <main class="box-front">
    <svg class="box-shapes" width="820" height="863" viewBox="0 0 820 863" aria-hidden="true">
      <rect class="top-band" x="0" y="0" width="820" height="104" fill="var(--box-lavender)"/>
      <path class="side-strip-left" fill="var(--box-lavender)"
        d="M0 104 H89 V436 L84.5 428 L80 436 L75.5 428 L71 436 L66.5 428 L62 436 L57.5 428 L53 436 L48.5 428 L44 436 L39.5 428 L35 436 L30.5 428 L26 436 L21.5 428 L17 436 L12.5 428 L8 436 L3.5 428 L0 436 Z"/>
      <path class="side-strip-right" fill="var(--box-lavender)"
        d="M731 104 H820 V436 L815.5 428 L811 436 L806.5 428 L802 436 L797.5 428 L793 436 L788.5 428 L784 436 L779.5 428 L775 436 L770.5 428 L766 436 L761.5 428 L757 436 L752.5 428 L748 436 L743.5 428 L739 436 L734.5 428 L731 436 Z"/>
      <g class="panel-frame" stroke="var(--frame-lavender)" stroke-width="3" fill="none">
        <path d="M87.5 430 V649 H305"/>
        <path d="M528 649 H732.5 V430"/>
      </g>
    </svg>

    <h1 class="brand-name">MORVEN</h1>
    <p class="product-line">BOTANICAL</p>
    <p class="product-type">RELIEVING BATH BOMB</p>
    <p class="tagline">small-batch crafted with intention and embodying natural butters,<br>salts, and beneficial botanical oils to relax and relieve the mind and body</p>

    <div class="botanical-art" role="img" aria-label="Watercolour bouquet of eucalyptus leaves and lavender sprigs over a soft lilac wash"></div>

    <p class="benefits">HYDRATE INDULGE PAMPER RELIEVE</p>

    <footer class="info-band">500 MG CBD NET WT. 135 G (4.76 oz)</footer>
  </main>
</body>
</html>
```